Flyer-Design für Wohn -und Einrichtungsberaterin
Zielgruppe
Ich bin eine Wohn -und Einrichtungsberaterin und biete neben der Wohnraumopitimierung auch Gartenberatung und Workshops an. Ich bin gelernte Floristin und habe daher einen engen Bezug zur Natürlichkeit.
Aufgabenstellung
Mein Flyer soll die Größe 148 x 148mm haben, mit einer klaren und ruhigen Erscheinung. Das Farbkonzept sollte sich in natürlichen und gedeckten Erdtönen wiederfinden. Trotzdem soll das Konzept ausdrucksstark präsentiert werden.
Vorderseite:
-transparentes Wohnbild im Hintergrund, darauf das Logo
-Bild (Tisch) und Logo siehe Anhänge
Rückseite:
-4 quadratische Textwürfel 2x2 angeordnet (neben- und untereinander)
1. Würfel (oben links)
Überschrift: WOHNRAUMGESTALTUNG
Text: Mit der vorhandenen Einrichtung eine Verbesserung des Wohngefühls schaffen.
2. Würfel (oben rechts)
Überschrift:GARTENBERATUNG
Text: Durch Anregung in der Garten -und Terassengestaltung ein neues Erscheinungsbild kreieren.
3. Würfel (unten links)
Überschrift: RAUMDESIGN
Text: In Praxis- und Gewerberäumen eine neue Atmosphäre erzielen.
4.Würfel (unten rechts)
Überschrift: WORKSHOPS
Text: Kreative Gruppenevents zu verschiedensten Anlässen und Themen erleben.

```html
<!DOCTYPE html>
<html lang="de">
<head>
<meta charset="utf-8">
<title>Raumatelier – Flyer Vorder- und Rückseite</title>
<link href="https://fonts.googleapis.com/css2?family=Roboto:wght@300;400;500;700&display=swap" rel="stylesheet">
<style>
  :root {
    --bg: #2a2a2a;
    --teal: #44676b;
    --teal-veil: rgba(68, 103, 107, 0.78);
    --paper: #f6f5f1;
    --heading: #3f7a6e;
    --body-text: #4a4a4a;
    --wood: #8a6a4a;
    --white: #ffffff;
  }
  * { box-sizing: border-box; margin: 0; padding: 0; }
  html, body {
    width: 1200px; height: 1200px; overflow: hidden;
    background: var(--bg);
    font-family: "Roboto", sans-serif;
  }
  .stage {
    position: relative; width: 1200px; height: 1200px;
    display: flex; align-items: center; justify-content: center; gap: 40px;
  }
  .flyer {
    position: relative; width: 540px; height: 540px;
    box-shadow: 0 18px 40px rgba(0,0,0,0.45);
  }

  /* Front */
  .flyer-front { overflow: hidden; }
  .front-photo {
    position: absolute; inset: 0;
    background:
      radial-gradient(circle at 60% 25%, rgba(70,120,115,0.7) 0 14%, transparent 32%),
      radial-gradient(circle at 80% 70%, rgba(230,230,225,0.8) 0 10%, transparent 30%),
      linear-gradient(160deg, #2f3a30 0%, #5c4a35 35%, #a07c55 55%, #8a8a85 78%, #c9c8c3 100%);
  }
  .front-veil {
    position: absolute; left: 150px; top: 120px; width: 300px; height: 300px;
    background: var(--teal-veil);
    color: var(--white);
    padding: 40px 28px 0;
    text-align: center;
  }
  .brand-name {
    font-weight: 300; font-size: 34px; letter-spacing: 3px; text-transform: uppercase;
  }
  .brand-mark {
    display: inline-block; width: 10px; height: 10px; background: var(--white);
    margin-top: 12px;
  }
  .contact { margin-top: 34px; font-size: 13px; line-height: 1.6; font-weight: 300; }
  .contact .person { font-weight: 500; font-size: 15px; letter-spacing: 0.5px; margin-bottom: 6px; }
  .contact .label { font-weight: 500; }

  /* Back */
  .flyer-back {
    background: var(--teal);
    padding: 40px;
    display: grid;
    grid-template-columns: 1fr 1fr;
    grid-template-rows: 1fr 1fr;
    gap: 14px;
  }
  .service-tile {
    background: var(--paper);
    display: flex; flex-direction: column; align-items: center; justify-content: center;
    text-align: center; padding: 18px 22px;
  }
  .service-icon { width: 70px; height: 64px; margin-bottom: 14px; }
  .service-title {
    color: var(--heading); font-weight: 700; font-size: 14px; letter-spacing: 0.6px;
    margin-bottom: 8px;
  }
  .service-text { color: var(--body-text); font-size: 12px; line-height: 1.4; }
</style>
</head>
<body>
<main class="stage">

  <section class="flyer flyer-front" aria-label="Flyer Vorderseite">
    <div class="front-photo" role="img" aria-label="Foto eines Wohnraums mit Holztisch, Stühlen und grünen Dekovasen"></div>
    <div class="front-veil">
      <div class="brand-name">Raumatelier</div>
      <span class="brand-mark"></span>
      <div class="contact">
        <div class="person">LUNO MEVERDASPI</div>
        <div><span class="label">Mobil</span> 0151 2048376</div>
        <div><span class="label">Mail</span> luno.meverdaspi@post.de</div>
        <div class="label">www.raumatelier-beratung.de</div>
      </div>
    </div>
  </section>

  <section class="flyer flyer-back" aria-label="Flyer Rückseite">
    <article class="service-tile">
      <svg class="service-icon" role="img" aria-label="Illustration Stehlampe und Sessel" viewBox="0 0 70 64">
        <rect x="6" y="6" width="58" height="52" rx="8" fill="#c7a58c"/>
      </svg>
      <h2 class="service-title">WOHNRAUMGESTALTUNG</h2>
      <p class="service-text">Mit der vorhandenen Einrichtung eine Verbesserung des Wohngefühls schaffen.</p>
    </article>
    <article class="service-tile">
      <svg class="service-icon" role="img" aria-label="Illustration Baum" viewBox="0 0 70 64">
        <rect x="6" y="6" width="58" height="52" rx="8" fill="#5f8a86"/>
      </svg>
      <h2 class="service-title">GARTENBERATUNG</h2>
      <p class="service-text">Durch Anregung in der Garten- und Terassengestaltung ein neues Erscheinungsbild kreieren.</p>
    </article>
    <article class="service-tile">
      <svg class="service-icon" role="img" aria-label="Illustration Tischleuchte und Blumenvase" viewBox="0 0 70 64">
        <rect x="6" y="6" width="58" height="52" rx="8" fill="#3f6f6a"/>
      </svg>
      <h2 class="service-title">RAUMDESIGN</h2>
      <p class="service-text">In Praxis- und Gewerberäumen eine neue Atmosphäre erzielen.</p>
    </article>
    <article class="service-tile">
      <svg class="service-icon" role="img" aria-label="Illustration gekreuzter Bleistift und Pinsel" viewBox="0 0 70 64">
        <rect x="6" y="6" width="58" height="52" rx="8" fill="#c7a58c"/>
      </svg>
      <h2 class="service-title">WORKSHOPS</h2>
      <p class="service-text">Kreative Gruppenevents zu verschiedensten Anlässen und Themen erleben.</p>
    </article>
  </section>

</main>
</body>
</html>
```